Tour agency for FIT and groups need a business card design

We need a business card design for a tour agency company that is based in Perth called" BRISK NO", we aim to provide customise, unique and seamless travel arrangement for FIT and groups. We serve both high profile businessperson, government authorities, business partners, executives and investors. The name card should be more professional looking.
Updates

Project Deadline Extended Reason: Have some changes that needed to make, director will be back to office on Monday, sorry for the inconvenience cause. Added Saturday, May 6, 2017

Target Market(s)

High profile businessperson, government authorities, business partners, executives and investors.

Industry/Entity Type

Tourism

Contact Information for Business Card

Brisk NO
Level 1, 214 Marlowe Avenue, Dunreath NO, 6120
www.briskno.com.au

Font styles to use
Serif

Colors

Designer to choose colors to be used in the design.

Requirements
Must have
• My project must have a company logo
Nice to have
• a more professional and solid yet friendly name card design. We may want to include chinese name in the name card as well. Edge of the card can be filled with gold and we think that transparent name cards are interesting.

```html
<!DOCTYPE html>
<html lang="en">
<head>
<meta charset="utf-8">
<title>Brisk NO – Business Card</title>
<link href="https://fonts.googleapis.com/css2?family=Nunito:wght@400&family=Raleway:wght@300;400&family=Noto+Serif+SC:wght@400&display=swap" rel="stylesheet">
<style>
  :root {
    --page-bg: #ffffff;
    --label-ink: #1a1a1a;
    --card-top: #3d9ddc;
    --card-mid: #2a7cc8;
    --card-deep: #1c55a8;
    --card-ink: #e9f1fa;
    --card-ink-soft: rgba(233, 241, 250, 0.72);
    --rule: rgba(233, 241, 250, 0.8);
    --brand-ink: #c9d3de;
  }
  * { margin: 0; padding: 0; box-sizing: border-box; }
  html, body {
    width: 1200px;
    height: 1000px;
    overflow: hidden;
    background: var(--page-bg);
  }
  .canvas {
    position: relative;
    width: 1200px;
    height: 1000px;
  }
  .side-label {
    position: absolute;
    left: 0;
    width: 300px;
    text-align: right;
    padding-right: 2px;
    font-family: "Nunito", "Helvetica Neue", sans-serif;
    font-size: 31px;
    color: var(--label-ink);
    letter-spacing: 0.5px;
  }
  .side-label--front { top: 244px; }
  .side-label--back { top: 700px; left: -13px; }

  .card {
    position: absolute;
    left: 454px;
    width: 359px;
    height: 205px;
    overflow: hidden;
  }
  .card--front { top: 161px; }
  .card--back { top: 612px; }

  .card__photo {
    position: absolute;
    inset: 0;
    background:
      radial-gradient(ellipse 60% 80% at 80% 80%, rgba(28, 60, 150, 0.55), transparent 70%),
      linear-gradient(160deg, var(--card-top) 0%, var(--card-mid) 45%, var(--card-deep) 100%);
  }

  .brand {
    position: absolute;
    left: 0;
    right: 0;
    top: 94px;
    display: flex;
    justify-content: center;
    align-items: center;
    gap: 8px;
    font-family: "Raleway", "Helvetica Neue", sans-serif;
    font-weight: 400;
    font-size: 22px;
    color: var(--brand-ink);
    letter-spacing: 1px;
  }
  .brand__dot {
    width: 8px;
    height: 8px;
    border-radius: 50%;
    background: var(--brand-ink);
  }

  .identity {
    position: absolute;
    left: 30px;
    top: 66px;
    width: 150px;
    text-align: center;
  }
  .identity__cn {
    font-family: "Noto Serif SC", serif;
    font-size: 26px;
    color: var(--card-ink);
    letter-spacing: 4px;
    line-height: 1.1;
  }
  .identity__en {
    font-family: "Raleway", "Helvetica Neue", sans-serif;
    font-weight: 300;
    font-size: 13px;
    color: var(--card-ink-soft);
    margin-top: 1px;
  }
  .divider {
    position: absolute;
    left: 184px;
    top: 49px;
    width: 1px;
    height: 96px;
    background: var(--rule);
  }
  .contacts {
    position: absolute;
    left: 215px;
    top: 72px;
    list-style: none;
    font-family: "Raleway", "Helvetica Neue", sans-serif;
    font-weight: 300;
    font-size: 9px;
    color: var(--card-ink-soft);
  }
  .contacts__item {
    display: flex;
    align-items: center;
    gap: 9px;
    height: 20px;
    margin-bottom: 5px;
  }
  .contacts__icon { width: 15px; height: 18px; flex: none; }
  .web {
    position: absolute;
    left: 0;
    right: 0;
    bottom: 9px;
    text-align: center;
    font-family: "Raleway", "Helvetica Neue", sans-serif;
    font-weight: 300;
    font-size: 9px;
    color: rgba(233, 241, 250, 0.45);
  }
</style>
</head>
<body>
<main class="canvas">
  <div class="side-label side-label--front">FRONT</div>
  <section class="card card--front">
    <div class="card__photo" role="img" aria-label="Translucent blue card tint over a city skyline photograph"></div>
    <div class="brand">
      <span class="brand__dot"></span>
      <span class="brand__name">Brisk NO</span>
    </div>
  </section>

  <div class="side-label side-label--back">BACK</div>
  <section class="card card--back">
    <div class="card__photo" role="img" aria-label="Translucent blue card tint over a city skyline photograph"></div>
    <div class="identity">
      <div class="identity__cn" lang="zh">迅诺行</div>
      <div class="identity__en">Brisk NO</div>
    </div>
    <div class="divider"></div>
    <ul class="contacts">
      <li class="contacts__item">
        <svg class="contacts__icon" viewBox="0 0 16 16" fill="none" stroke="#e9f1fa" stroke-width="1.1">
          <circle cx="8" cy="8" r="6.5"/>
          <circle cx="8" cy="8" r="2.6"/>
          <path d="M10.6 5.6v3.6c0 1.2 1.9 1.3 1.9-.6"/>
        </svg>
        <span>info@briskno.com.au</span>
      </li>
      <li class="contacts__item">
        <svg class="contacts__icon" viewBox="0 0 16 20" fill="none" stroke="#e9f1fa" stroke-width="1.1">
          <rect x="3" y="1" width="10" height="18" rx="1.5"/>
          <line x1="3" y1="4" x2="13" y2="4"/>
          <line x1="3" y1="16" x2="13" y2="16"/>
        </svg>
        <span>+08 900 123 4567</span>
      </li>
    </ul>
    <div class="web">www.briskno.com.au</div>
  </section>
</main>
</body>
</html>
```